【依頼の目的/概要】
電子書籍(pavlo)の表紙デザインをお願いします

【画像サイズ】
*RVSより抜粋
表紙ファイルの理想的な寸法は2,560×1,600ピクセルです。
注:画像の寸法は1,000×625ピクセル以上であることが必要です
画像の最大の寸法は10,000×10,000ピクセルです

【タイトル】
朝の庭で見つけた小さな灯りの話

サブキャッチ
~来場者2倍、満足度9割の老舗書店を育てた5つの習慣

【著者】
ミドリノタネ工房代表
組織進化コンサルタント
柳瀬 公平

【本の内容】
とても勤勉で勉強家の開業歯科医のみなさんが
がんばってもなかなか成果の出づらい分野、
「チーム創り」について。

まず互いを人として大事にすることで
スタッフが自然に結束し、
「ここで働けてよかった」
と思うようになる。
楽しいから自主的創造的に動くようになる。
すると成果の質も高くなる。
そうなるまでのステップを紹介。

著者はレポートを出す型のコンサルではなく、
現場に入り込んでゲーム性の高い体験型研修や
一人一人の話を聴いて言葉にならない本音を通訳することなどが得意。
愛と遊び心をもってプログラムを提供し伴走するので
笑顔が絶えることがない。

*参考資料として原稿を添付します

【デザイン要望】
特にイメージにこだわりはありませんので
自由な発想でのデザインご応募を楽しみにしています。

*次点、次々点の方への参加報酬を設定いたしました。

*その他、必要な情報がありましたらお問い合わせください。

スマホでpavloを見るとき、小さなアイコンが並ぶ中で最も目に留まるデザインで、
一目で重要なワードも目に入るデザインだったので採用させていただきました。

次点の二つについても同様の基準でしたが
色使いやフォントサイズなどを調整して、
もっとパッと目に入るものでしたら順序が変わったかもしれません。

特に、チームがテーマなので人の写真+見やすいデザインが両方だったらよりよかったかなと思います

皆さま、一所懸命やっていただいてありがとうございました。
こんなにもたくさんの方にご提案いただけてとてもうれしいです。
お礼を出せるのは3作品ですが
皆様にお礼を改めて申し上げたいと思います。

電子書籍の売れ行きにとても大事な表紙づくりのご協力、本当にありがとうございました。

```html
<!DOCTYPE html>
<html lang="ja">
<head>
<meta charset="utf-8">
<title>朝の庭で見つけた小さな灯りの話</title>
<link rel="stylesheet" href="https://fonts.googleapis.com/css2?family=M+PLUS+1p:wght@700;800;900&family=Noto+Serif+JP:wght@500&display=swap">
<style>
  :root {
    --ink-blue: #1f6fd1;
    --sky: #55c4f3;
    --band: #1b6cd4;
    --white: #ffffff;
    --accent-yellow: #f5c21a;
    --text-dark: #2a2a2a;
    --tone-warm: #f2b23a;
    --tone-red: #d8435a;
    --tone-cool: #2aa6b8;
    --tone-green: #3aa866;
  }
  * { margin: 0; padding: 0; box-sizing: border-box; }
  html, body { width: 750px; height: 1200px; overflow: hidden; background: var(--white); }
  .cover {
    position: relative; width: 750px; height: 1200px; overflow: hidden;
    background: var(--white);
    font-family: "M PLUS 1p", sans-serif;
  }
  .title { position: absolute; top: 40px; left: 0; width: 100%; text-align: center; }
  .title-line {
    color: var(--ink-blue); font-weight: 800; font-size: 70px; line-height: 1;
    letter-spacing: 2px;
  }
  .title-line + .title-line { margin-top: 22px; }
  .em { position: relative; display: inline-block; }
  .em::before {
    content: ""; position: absolute; top: -16px; left: 50%;
    width: 14px; height: 14px; margin-left: -7px; border-radius: 50%;
    background: var(--accent-yellow);
  }
  .title-hero {
    margin-top: 24px;
    font-size: 108px; font-weight: 900; line-height: 1.05;
    color: var(--sky);
    font-style: italic;
    -webkit-text-stroke: 3px var(--white);
    text-shadow: 0 0 18px rgba(85,196,243,.55), 0 4px 10px rgba(31,111,209,.3);
    letter-spacing: 4px;
  }
  .team-visual {
    position: absolute; left: 187px; top: 383px; width: 376px; height: 376px;
    border-radius: 50%;
    background: linear-gradient(135deg, var(--tone-green) 0%, var(--tone-red) 35%, var(--tone-warm) 65%, var(--tone-cool) 100%);
    opacity: .85;
  }
  .author {
    position: absolute; top: 765px; left: 0; width: 100%; text-align: center;
    font-family: "Noto Serif JP", serif; font-weight: 500;
    color: var(--text-dark); font-size: 29px; line-height: 37px;
  }
  .band {
    position: absolute; left: 0; top: 918px; width: 750px; height: 282px;
    background: var(--band);
  }
  .catch-a {
    position: absolute; left: 10px; top: 18px;
    color: var(--white); font-weight: 800; font-size: 48px; line-height: 1; white-space: nowrap;
  }
  .catch-a .num { font-size: 66px; }
  .catch-b {
    position: absolute; left: 10px; top: 94px;
    color: var(--white); font-weight: 800; font-size: 56px; line-height: 70px; white-space: nowrap;
  }
  .catch-b .boxed {
    display: inline-block; background: var(--white); color: var(--band);
    padding: 0 4px;
  }
  .catch-c {
    position: absolute; left: 12px; top: 170px;
    color: var(--white); font-weight: 800; font-size: 62px; line-height: 1; white-space: nowrap;
  }
  .catch-c .num { font-size: 112px; }
  .mascot {
    position: absolute; left: 610px; top: 940px; width: 130px; height: 230px;
    border-radius: 60px 60px 40px 40px;
    background: linear-gradient(180deg, #ffffff 0%, #dbeefc 100%);
  }
</style>
</head>
<body>
<main class="cover">
  <header class="title">
    <p class="title-line">朝の庭で</p>
    <p class="title-line"><span class="em">見</span><span class="em">つ</span>けた小さな</p>
    <h1 class="title-line title-hero">灯りの話</h1>
  </header>

  <div class="team-visual" role="img" aria-label="色とりどりのパズルピースがつながった輪のイラスト"></div>

  <div class="author">
    <p>ミドリノタネ工房代表</p>
    <p>組織進化コンサルタント</p>
    <p>柳瀬 公平 著</p>
  </div>

  <section class="band">
    <p class="catch-a">来場者<span class="num">2</span>倍、満足度<span class="num">9</span>割の</p>
    <p class="catch-b"><span class="boxed">老舗書店</span>を育てた</p>
    <p class="catch-c"><span class="num">5</span>つの習慣</p>
  </section>

  <div class="mascot" role="img" aria-label="歯ブラシを持つマスコットキャラクター"></div>
</main>
</body>
</html>
```